BOOk cover for an existing ebook called Build Momentum At The Office

I have an existing cover that i dont like (too male and boring looking) see http://www.shelvaro.co.uk/Build-Momentum-At-The-Office-ebook/dp/K77Q4M1ZR3 I want something that blends with my existing brand colours Dark purple : 51 0 102 / 270 100 40 / #330066 this is purple

dark Grey: 136 136 136 / 0 0 53 / #888888

Mid: grey 101 20 152 / 281 85 53 / #651488

Light purple : 157 107 207/ 270 48 81 / #9d6bcf and 2 existing book covers See http://www.shelvaro.co.uk/HOW-WE-THINK-Joan-Brindle-ebook/dp/K77XH293W5 and a book in the attached image file. i'd like designs that blend with this cover and communicate - this is a toolkit get on with it.

```html
<!DOCTYPE html>
<html lang="en">
<head>
<meta charset="utf-8">
<title>Build Momentum At The Office — Book Cover</title>
<link rel="stylesheet" href="https://fonts.googleapis.com/css2?family=Montserrat:wght@600;700&display=swap">
<style>
  :root {
    --page-bg: #f4f4f4;
    --purple-deep: #5a2a8a;
    --purple-core: #632e93;
    --purple-edge: #5c2d88;
    --purple-glow: #9a80c0;
    --purple-base: #5f3d8c;
    --ink-light: #ffffff;
  }
  * { margin: 0; padding: 0; box-sizing: border-box; }
  html, body {
    width: 1200px;
    height: 1200px;
    overflow: hidden;
    background: var(--page-bg);
  }
  .cover {
    position: absolute;
    left: 256px;
    top: 54px;
    width: 688px;
    height: 1092px;
    overflow: hidden;
    background:
      radial-gradient(ellipse 330px 300px at 50% 29%, var(--purple-glow) 0%, rgba(154,128,192,0) 100%),
      radial-gradient(ellipse 600px 260px at 50% 100%, var(--purple-base) 0%, rgba(95,61,140,0) 100%),
      linear-gradient(180deg, var(--purple-deep) 0%, var(--purple-core) 55%, var(--purple-edge) 100%);
    color: var(--ink-light);
    font-family: "Montserrat", sans-serif;
    text-align: center;
  }
  .cover__author {
    position: absolute;
    left: 0;
    right: 0;
    top: 70px;
    font-size: 30px;
    font-weight: 700;
    letter-spacing: 0.32em;
    padding-left: 0.32em;
    line-height: 40px;
  }
  .cover__emblem {
    position: absolute;
    left: 232px;
    top: 160px;
    width: 226px;
    height: 270px;
    border-radius: 40px;
    background: radial-gradient(ellipse at 50% 50%, rgba(255,255,255,0.55) 0%, rgba(255,255,255,0.18) 60%, rgba(255,255,255,0) 100%);
  }
  .cover__title {
    position: absolute;
    left: 0;
    right: 0;
    top: 458px;
    font-size: 86px;
    font-weight: 700;
    line-height: 106px;
    letter-spacing: 0.005em;
    text-transform: uppercase;
  }
  .cover__title span { display: block; }
  .cover__subtitle {
    position: absolute;
    left: 0;
    right: 0;
    top: 920px;
    font-size: 26px;
    font-weight: 600;
    line-height: 39px;
  }
  .cover__subtitle span { display: block; }
</style>
</head>
<body>
  <main class="cover">
    <p class="cover__author">JOAN BRINDLE</p>
    <div class="cover__emblem" role="img" aria-label="Cover emblem illustration in white"></div>
    <h1 class="cover__title">
      <span>Build</span>
      <span>Momentum</span>
      <span>At The</span>
      <span>Office</span>
    </h1>
    <p class="cover__subtitle">
      <span>A Hands-On Plan</span>
      <span>Workplace Growth Playbook</span>
    </p>
  </main>
</body>
</html>
```